Business Image

I have recently had a new company logo made up and require some new business cards to go with it.

Target Market(s)

Developers & high worth clients.

Industry/Entity Type

Business

Contact Information for Business Card

The business is in the construction/management industry. It needs to be classy but have a industrial feel. I would like the business card to be a elegant presentation in itself.

Requirements
Must have
• Current logo & company name. Colouring needs to be the same as the current design also.
Nice to have
• A few different designs & presentations of single and double sided business cards.

```html
<!DOCTYPE html>
<html lang="en">
<head>
<meta charset="utf-8">
<title>Summit Build Group – Business Cards</title>
<link rel="stylesheet" href="https://fonts.googleapis.com/css2?family=Tinos:wght@700&family=Open+Sans:wght@400&display=swap">
<style>
  :root {
    --backdrop: #ecebe8;
    --brand-blue: #2a6fa8;
    --brand-blue-light: #3479b2;
    --brand-blue-deep: #2466a0;
    --card-white: #ffffff;
    --ink: #2b2b2b;
    --ink-soft: #4a4a4a;
    --tint: #e8eef5;
  }
  * { margin: 0; padding: 0; box-sizing: border-box; }
  html, body { width: 1200px; height: 900px; overflow: hidden; }
  body { background: var(--backdrop); position: relative; font-family: "Open Sans", sans-serif; }

  .card {
    position: absolute;
    width: 540px;
    height: 310px;
    box-shadow: 0 6px 18px rgba(0,0,0,0.18);
    overflow: hidden;
  }

  /* Front: blue */
  .card-front {
    left: 80px; top: 120px;
    background: linear-gradient(135deg, var(--brand-blue-light) 0%, var(--brand-blue) 50%, var(--brand-blue-deep) 100%);
  }
  .card-front .wordmark {
    position: absolute; left: 0; right: 0; top: 118px;
    display: flex; align-items: center; justify-content: center; gap: 12px;
  }
  .mark-square { width: 24px; height: 24px; background: var(--card-white); flex: none; }
  .company-name {
    font-family: "Tinos", serif; font-weight: 700;
    font-size: 30px; letter-spacing: 1px; color: var(--card-white);
    line-height: 1; white-space: nowrap;
  }
  .card-front .website {
    position: absolute; left: 0; right: 0; top: 182px;
    text-align: center; color: var(--card-white); font-size: 15px; letter-spacing: 0.3px;
  }

  /* Back: white */
  .card-back { left: 580px; top: 460px; background: var(--card-white); }
  .card-back .tint-block {
    position: absolute; right: -30px; top: 70px;
    width: 170px; height: 200px; background: var(--tint);
  }
  .card-back .wordmark {
    position: absolute; left: 40px; top: 40px;
    display: flex; align-items: center; gap: 10px;
  }
  .card-back .mark-square { background: var(--brand-blue); width: 20px; height: 20px; }
  .card-back .company-name { color: var(--brand-blue); font-size: 26px; }

  .holder { position: absolute; left: 40px; top: 110px; }
  .holder-name {
    font-family: "Tinos", serif; font-weight: 700; font-size: 20px;
    color: var(--brand-blue); letter-spacing: 0.5px;
  }
  .holder-title { font-size: 14px; color: var(--ink-soft); margin-top: 1px; }

  .contact { position: absolute; left: 40px; top: 172px; list-style: none; }
  .contact li {
    display: flex; align-items: center; gap: 9px;
    font-size: 14px; color: var(--ink); line-height: 21px;
  }
  .contact svg { width: 13px; height: 13px; fill: var(--brand-blue); flex: none; }
  .address { position: absolute; left: 40px; top: 245px; font-size: 14px; color: var(--ink); line-height: 21px; }
</style>
</head>
<body>

  <section class="card card-front" aria-label="Business card front">
    <div class="wordmark">
      <span class="mark-square"></span>
      <span class="company-name">SUMMIT BUILD GROUP</span>
    </div>
    <p class="website">www.summitbuild.com</p>
  </section>

  <section class="card card-back" aria-label="Business card back">
    <div class="tint-block"></div>
    <div class="wordmark">
      <span class="mark-square"></span>
      <span class="company-name">SUMMIT BUILD GROUP</span>
    </div>

    <div class="holder">
      <p class="holder-name">DANIEL HART</p>
      <p class="holder-title">Managing Director</p>
    </div>

    <ul class="contact">
      <li>
        <svg viewBox="0 0 16 16" aria-hidden="true"><path d="M4 0h8a1.5 1.5 0 0 1 1.5 1.5v13A1.5 1.5 0 0 1 12 16H4a1.5 1.5 0 0 1-1.5-1.5v-13A1.5 1.5 0 0 1 4 0zm0 2v10.5h8V2zm4 11.3a.9.9 0 1 0 0 1.8.9.9 0 0 0 0-1.8z"/></svg>
        044-555 018 234
      </li>
      <li>
        <svg viewBox="0 0 16 16" aria-hidden="true"><path d="M1 5c0-2 3-3 7-3s7 1 7 3v1.5h-3.5V5h-7v1.5H1zM3 8l2-2h6l2 2v6H3zm5 1.5a2 2 0 1 0 0 4 2 2 0 0 0 0-4z"/></svg>
        044-555 018 567
      </li>
      <li>
        <svg viewBox="0 0 16 16" aria-hidden="true"><path d="M1 3h14v10H1zm1.5 1.5v.3L8 9l5.5-4.2v-.3zm0 2.2v4.8h11V6.7L8 10.9z"/></svg>
        info@summitbuild.com
      </li>
    </ul>

    <p class="address">12345, Address Goes Here<br>Country Name, 123456.</p>
  </section>

</body>
</html>
```